DrivPeak Agile Coaching Website

I need an updated website for www.drivpeak.example. I'm looking for a modern look. This is a professional site, but I don't want it to look "stuffy". It needs to have an element of fun and learning.

My services include:
Lean Agile Coaching
Lean Agile Training
Facilitation
Workshops
Consulting

Ideas this site should convey: collaboration, learning, teamwork, adaptability, flow, limited WIP, agility, Lean.

I would like to use some of my own photos and slide decks for content: http://www.deckvault.example/mornbeck/presentations

I would also like to include the Peerlinko recommendations I have from customers: https://www.peerlinko.example/in/mornbeck

Examples of sites I like:
http://www.quarrelmosswidget.example
http://www.forthsprintly.example

Target Market(s)

IT professionals, software development managers

Industry/Entity Type

It Company

Coding

Coded - Design and coding required

Font styles to use
Serif
Sans Serif

Requirements
Must have
• Original looking graphics and layout.
• My logo must be included in layout.
• Need to feature my blog content.
• Deliverable must be a WordPress theme that I can install.
• Responsive site.
Nice to have
• Use images from my slides on Deckvault if they make sense.

```html
<!DOCTYPE html>
<html lang="en">
<head>
<meta charset="utf-8">
<title>DrivPeak – Lean Agile Coaching</title>
<link href="https://fonts.googleapis.com/css2?family=Raleway:wght@300;400;700&family=Arimo:wght@400;700&display=swap" rel="stylesheet">
<style>
:root{
  --green:#1fc14a;
  --ink:#222;
  --text:#555;
  --muted:#666;
  --band:#f3f3f3;
  --white:#fff;
  --footer:#262626;
  --footer-line:#3a3a3a;
}
*{margin:0;padding:0;box-sizing:border-box}
html,body{width:1200px;height:3462px;overflow:hidden;background:var(--white)}
body{position:relative;font-family:"Arimo",Arial,sans-serif;color:var(--text)}

/* header */
.site-header{position:absolute;left:0;top:0;width:1200px;height:85px;background:var(--white)}
.brand-name{position:absolute;left:78px;top:18px;font-family:"Raleway",sans-serif;font-weight:700;font-size:42px;line-height:50px;color:var(--ink)}
.main-nav{position:absolute;top:30px;left:634px;font-size:16px}
.main-nav a{position:absolute;white-space:nowrap;text-decoration:none;color:#333}
.main-nav .active{color:var(--green)}
.search-icon{position:absolute;left:1078px;top:33px}

/* hero */
.hero{position:absolute;left:0;top:85px;width:1200px;height:591px;
  background:linear-gradient(160deg,#4a3a30 0%,#2f2a28 40%,#55493f 70%,#3a332e 100%)}
.hero-notch{position:absolute;left:530px;top:676px;width:140px;height:28px;background:#3a332e;clip-path:polygon(0 0,100% 0,50% 100%)}
.hero-title{position:absolute;left:0;top:238px;width:1200px;text-align:center;font-family:"Raleway",sans-serif;font-weight:300;font-size:82px;color:var(--white);letter-spacing:2px}
.hero-text{position:absolute;left:230px;top:352px;width:740px;text-align:center;color:var(--white);font-size:19px;line-height:31px}
.hero-btn{position:absolute;left:508px;top:482px;width:180px;height:49px;background:var(--green);clip-path:polygon(0 0,88% 0,100% 50%,88% 100%,0 100%);color:var(--white);font-weight:700;font-size:15px;line-height:49px;padding-left:34px;letter-spacing:.5px}

/* about */
.section-title{position:absolute;left:0;width:1200px;text-align:center;font-family:"Raleway",sans-serif;font-weight:400;font-size:42px;color:var(--ink)}
.about-text{position:absolute;left:130px;width:940px;text-align:center;font-size:14px;line-height:25px;color:var(--muted)}
.about-text strong{color:#444}

/* services */
.service{position:absolute;left:0;width:1200px;height:364px;background:var(--band);overflow:hidden}
.service .photo{position:absolute;top:0;height:364px}
.photo-left{left:0;width:669px;clip-path:polygon(0 0,588px 0,669px 50%,588px 100%,0 100%)}
.photo-right{left:538px;width:662px;clip-path:polygon(80px 0,662px 0,662px 100%,80px 100%,0 50%)}
.service-copy{position:absolute;width:418px;top:50px}
.copy-right{left:708px}
.copy-left{left:72px;text-align:right}
.service-icon{display:block;width:46px;height:46px}
.copy-left .service-icon{margin-left:auto}
.service-title{font-family:"Raleway",sans-serif;font-weight:400;font-size:32px;color:var(--ink);margin:8px 0 14px}
.service-body{font-size:14px;line-height:24px;color:var(--muted)}

/* blog */
.blog-card{position:absolute;top:2949px;width:334px}
.blog-photo{width:334px;height:166px}
.blog-meta{position:relative;margin-top:12px;padding-left:66px;min-height:120px}
.date-box{position:absolute;left:0;top:0;width:55px;height:62px;background:var(--green);color:var(--white);text-align:center}
.date-box .day{display:block;font-size:24px;line-height:30px;padding-top:3px}
.date-box .mon{display:block;font-size:17px;line-height:22px}
.blog-title{font-weight:700;font-size:16px;line-height:23px;color:#111}
.blog-excerpt{margin-top:4px;font-size:13.5px;line-height:21px;color:var(--muted)}
.read-more{display:block;margin-top:6px;font-size:14px;color:#333}
.read-more.accent{color:var(--green)}

/* footer */
.site-footer{position:absolute;left:0;top:3325px;width:1200px;height:137px;background:var(--footer)}
.footer-nav{position:absolute;left:78px;top:26px;font-size:13px}
.footer-nav a{text-decoration:none;color:#777;margin-right:26px}
.footer-nav a.active{color:var(--white)}
.footer-rule{position:absolute;left:0;top:72px;width:1200px;height:1px;background:var(--footer-line)}
.copyright{position:absolute;left:0;top:98px;width:1200px;text-align:center;color:var(--white);font-family:"Raleway",sans-serif;font-weight:700;font-size:13px}
.copyright span{color:var(--green)}
.social{position:absolute;top:13px;width:44px;height:44px;border-radius:50%;border:2px solid var(--green)}
.social.light{border-color:var(--white)}
</style>
</head>
<body>

<header class="site-header">
  <span class="brand-name">DrivPeak</span>
  <nav class="main-nav">
    <a class="active" style="left:0">Home</a>
    <a style="left:108px">About</a>
    <a style="left:214px">Services</a>
    <a style="left:342px">Contact</a>
  </nav>
  <svg class="search-icon" width="18" height="18" viewBox="0 0 18 18"><circle cx="7.5" cy="7.5" r="5" fill="none" stroke="#1fc14a" stroke-width="2.5"/><line x1="11" y1="11" x2="16" y2="16" stroke="#1fc14a" stroke-width="3" stroke-linecap="round"/></svg>
</header>

<section class="hero" role="img" aria-label="Team gathered around a table planning with sticky notes and cards"></section>
<div class="hero-notch"></div>
<h1 class="hero-title">UNDERSTANDING</h1>
<p class="hero-text">Regardless if you are new to Agile and Lean, or your organization is now doing Agile, a better understanding of the principles and practices is crucial for team and organizational improvement.</p>
<div class="hero-btn">LEARN MORE</div>

<h2 class="section-title" style="top:732px">About DrivPeak</h2>
<p class="about-text" style="top:798px">DrivPeak is a company dedicated to improving the art and science of software development for both the consumers of software services and the professionals doing the work. Our primary focus is the marketplace and community where we live–the Kansas City metro area.</p>
<p class="about-text" style="top:867px">Our specialty is helping software organizations learn about and implement Lean-Agile approaches to software development. This includes Kanban, Scrum and Agile team practices, and XP technical practices.</p>
<p class="about-text" style="top:936px"><strong>DrivPeak starts with clarity and understanding. Understand where you are now, and clarity around where you want to be tomorrow.</strong></p>

<section class="service" style="top:1011px">
  <div class="photo photo-left" role="img" aria-label="Team working around a wooden table with laptops and charts" style="background:linear-gradient(135deg,#9a6a45,#b98a60 50%,#7a5640)"></div>
  <div class="service-copy copy-right">
    <svg class="service-icon" viewBox="0 0 46 46" fill="#1fc14a"><rect x="20" y="4" width="6" height="6"/><rect x="14" y="14" width="6" height="6"/><rect x="26" y="14" width="6" height="6"/><rect x="8" y="24" width="6" height="6"/><rect x="20" y="24" width="6" height="6"/><rect x="32" y="24" width="6" height="6"/><rect x="2" y="34" width="42" height="8"/></svg>
    <h3 class="service-title">Lean Agile Coaching</h3>
    <p class="service-body">Lorem Ipsum is simply dummy text of the printing and typesetting industry. Lorem Ipsum has been the industry's standard dummy text ever since the 1500s, when an unknown printer took a galley of type and scrambled it to make a type specimen book. It has survived not only five centuries, but also the leap into electronic typesetting.</p>
  </div>
</section>

<section class="service" style="top:1378px">
  <div class="photo photo-right" role="img" aria-label="Hands arranging colourful sticky notes on a table" style="background:linear-gradient(135deg,#8a8a88,#c9c4b8 55%,#e4d9a8)"></div>
  <div class="service-copy copy-left">
    <svg class="service-icon" viewBox="0 0 46 46" fill="none" stroke="#1fc14a" stroke-width="3"><rect x="6" y="4" width="34" height="24"/><line x1="12" y1="12" x2="30" y2="12"/><line x1="12" y1="19" x2="24" y2="19"/><line x1="14" y1="28" x2="8" y2="42"/><line x1="32" y1="28" x2="38" y2="42"/></svg>
    <h3 class="service-title">Lean Agile Training</h3>
    <p class="service-body">Lorem Ipsum is simply dummy text of the printing and typesetting industry. Lorem Ipsum has been the industry's standard dummy text ever since the 1500s, when an unknown printer took a galley of type and scrambled it to make a type specimen book. It has survived not only five centuries, but also the leap into electronic typesetting.</p>
  </div>
</section>

<section class="service" style="top:1742px">
  <div class="photo photo-left" role="img" aria-label="Facilitator drawing on a whiteboard in front of a group" style="background:linear-gradient(135deg,#dfe3e6,#c7cbd0 50%,#6f9c98)"></div>
  <div class="service-copy copy-right">
    <svg class="service-icon" viewBox="0 0 46 46" fill="none" stroke="#1fc14a" stroke-width="3"><rect x="16" y="4" width="26" height="20"/><polyline points="20,19 26,13 30,16 38,8"/><line x1="10" y1="28" x2="10" y2="42"/><line x1="4" y1="28" x2="16" y2="28"/></svg>
    <h3 class="service-title">Facilitation</h3>
    <p class="service-body">Lorem Ipsum is simply dummy text of the printing and typesetting industry. Lorem Ipsum has been the industry's standard dummy text ever since the 1500s, when an unknown printer took a galley of type and scrambled it to make a type specimen book. It has survived not only five centuries, but also the leap into electronic typesetting.</p>
  </div>
</section>

<section class="service" style="top:2107px">
  <div class="photo photo-right" role="img" aria-label="Business team meeting around a bright conference table" style="background:linear-gradient(135deg,#e8ecef,#b8c0c8 50%,#5c6470)"></div>
  <div class="service-copy copy-left">
    <svg class="service-icon" viewBox="0 0 46 46" fill="#1fc14a"><rect x="4" y="14" width="10" height="16"/><rect x="18" y="14" width="10" height="16"/><rect x="32" y="14" width="10" height="16"/><rect x="2" y="32" width="42" height="4"/><rect x="6" y="36" width="3" height="8"/><rect x="37" y="36" width="3" height="8"/></svg>
    <h3 class="service-title">Workshops</h3>
    <p class="service-body">Lorem Ipsum is simply dummy text of the printing and typesetting industry. Lorem Ipsum has been the industry's standard dummy text ever since the 1500s, when an unknown printer took a galley of type and scrambled it to make a type specimen book. It has survived not only five centuries, but also the leap into electronic typesetting.</p>
  </div>
</section>

<section class="service" style="top:2471px">
  <div class="photo photo-left" role="img" aria-label="Two consultants in suits reviewing a tablet" style="background:linear-gradient(135deg,#2f3a4a,#55657a 50%,#8a98a8)"></div>
  <div class="service-copy copy-right">
    <svg class="service-icon" viewBox="0 0 46 46" fill="#1fc14a"><rect x="14" y="4" width="26" height="16"/><polygon points="18,20 24,20 18,26"/><rect x="6" y="26" width="12" height="16"/><rect x="20" y="34" width="22" height="4"/></svg>
    <h3 class="service-title">Consulting</h3>
    <p class="service-body">Lorem Ipsum is simply dummy text of the printing and typesetting industry. Lorem Ipsum has been the industry's standard dummy text ever since the 1500s, when an unknown printer took a galley of type and scrambled it to make a type specimen book. It has survived not only five centuries, but also the leap into electronic typesetting.</p>
  </div>
</section>

<h2 class="section-title" style="top:2880px">Latest Blog</h2>

<article class="blog-card" style="left:76px">
  <div class="blog-photo" role="img" aria-label="Colleagues working together in an office" style="background:linear-gradient(135deg,#3e3a36,#7a7068 60%,#a59b90)"></div>
  <div class="blog-meta">
    <div class="date-box"><span class="day">05</span><span class="mon">Apr</span></div>
    <h4 class="blog-title">Lorem ipsum is simply dummy text of the printing</h4>
    <p class="blog-excerpt">Lorem Ipsum is simply dummy text of the printing and typesetting industry. Lorem Ipsum has been the industry's</p>
    <a class="read-more accent">READ MORE</a>
  </div>
</article>

<article class="blog-card" style="left:434px">
  <div class="blog-photo" role="img" aria-label="City skyline at dusk with glowing streets" style="background:linear-gradient(135deg,#1d3550,#3d5f80 50%,#c98a45)"></div>
  <div class="blog-meta">
    <div class="date-box"><span class="day">05</span><span class="mon">Apr</span></div>
    <h4 class="blog-title">Lorem ipsum is simply dummy text of the printing</h4>
    <p class="blog-excerpt">Lorem Ipsum is simply dummy text of the printing and typesetting industry. Lorem Ipsum has been the industry's</p>
    <a class="read-more">READ MORE</a>
  </div>
</article>

<article class="blog-card" style="left:789px">
  <div class="blog-photo" role="img" aria-label="Hand writing notes beside a phone on a desk" style="background:linear-gradient(135deg,#cfc8bd,#e8e2d8 55%,#6a6560)"></div>
  <div class="blog-meta">
    <div class="date-box"><span class="day">05</span><span class="mon">Apr</span></div>
    <h4 class="blog-title">Lorem ipsum is simply dummy text of the printing</h4>
    <p class="blog-excerpt">Lorem Ipsum is simply dummy text of the printing and typesetting industry. Lorem Ipsum has been the industry's</p>
    <a class="read-more">READ MORE</a>
  </div>
</article>

<footer class="site-footer">
  <nav class="footer-nav">
    <a class="active">Home</a><a>About Us</a><a>Services</a><a>Contact Us</a>
  </nav>
  <span class="social" style="left:1027px" aria-label="Social link"></span>
  <span class="social light" style="left:1080px" aria-label="Feed link"></span>
  <div class="footer-rule"></div>
  <p class="copyright">© <span>DrivPeak</span> - 2016. All Rights Reserved</p>
</footer>

</body>
</html>
```